Eco conscious print and frame company needs a website

‘LUMAeco is a new company that makes frames and fine art prints from sustainable bamboo. Our site should have an organic feel yet still have a professional clean look to it as well.
We need shopping cart and image uploading capabilities much like a pictorama or glowbird type of site only on a much smaller scale.
Currently we have 3 different styles available in sizes from 8"x8" all the way to 4ft by 8ft.
Target audience will be the snapvintra, pixelgram, zephone market.

Target Market(s)

20-40 years old male and female. Pixelgram generation.

Industry/Entity Type

Shopping

Requirements
Must have
• Front end and back end capabilities with emphasis on image uploading and shopping cart functionality.

```html
<!DOCTYPE html>
<html lang="en">
<head>
<meta charset="utf-8">
<title>LUMAeco Frame Company – Customize</title>
<link href="https://fonts.googleapis.com/css2?family=Open+Sans:wght@400;600&family=Oswald:wght@400;500&display=swap" rel="stylesheet">
<style>
:root{
  --bg:#e6e6e8;
  --panel:#ffffff;
  --panel-inner:#f2f2f3;
  --text:#3a3a3a;
  --muted:#9a9a9a;
  --green:#4d8f12;
  --green-bright:#7cbf2a;
  --green-dark:#3e7a10;
  --line:#d4d4d4;
  --wood:#e9c9ab;
  --wood-dark:#8c4f34;
  --footer-wood:#e6b36e;
}
*{box-sizing:border-box;margin:0;padding:0}
html,body{width:1200px;height:1200px;overflow:hidden}
body{background:var(--bg);font-family:"Open Sans",Arial,sans-serif;color:var(--text);position:relative}
.abs{position:absolute}
.caps{text-transform:uppercase;letter-spacing:1.4px;font-size:12.5px}
.green{color:var(--green)}

.site-header{left:110px;top:-10px;width:978px;height:118px;background:linear-gradient(100deg,#e4e4e6 0%,#fbfbfb 45%,#fff 55%,#e8e8ea 100%);border:5px solid #fff;border-top:none;border-radius:0 0 16px 16px;box-shadow:0 2px 4px rgba(0,0,0,.12)}
.nav-left{left:145px;top:35px;display:flex;gap:18px}
.nav-right{right:140px;top:35px;word-spacing:2px}
.brand{left:548px;top:56px;display:flex;align-items:center;gap:6px;font-size:22px;font-weight:600;color:var(--green)}
.brand-dot{width:14px;height:14px;border-radius:50%;background:var(--green-bright)}

.breadcrumb{left:145px;top:133px}

.steps{left:250px;top:184px}

.workspace{left:107px;top:262px;width:981px;height:488px;background:var(--panel-inner);border:7px solid var(--panel);border-radius:14px;box-shadow:0 2px 3px rgba(0,0,0,.12)}
.toolbar{left:125px;top:283px;width:945px;height:37px;background:linear-gradient(#fff,#f0f0f0);border-bottom:1px solid var(--line)}
.toolbar-label{left:144px;top:293px}
.tool-icons{left:433px;top:288px}
.btn-next{left:940px;top:281px;width:131px;height:39px;background:linear-gradient(#7fc22e,#55a015);border:1px solid var(--green-dark);border-radius:2px;font-family:"Oswald",sans-serif;font-size:20px;letter-spacing:2px;color:#2b4a0c;text-align:center;line-height:36px}

.sidebar-head{left:125px;top:320px;width:245px;height:41px;background:linear-gradient(#c8c8ca,#b9b9bb)}
.select{left:197px;top:329px;width:159px;height:24px;background:#fff;border:1px solid #ccc}
.select::after{content:"";position:absolute;right:6px;top:10px;border:4px solid transparent;border-top:5px solid #777}
.moulding-list{left:125px;top:365px;width:235px;height:378px;background:#fff}
.moulding{position:absolute;left:9px;width:208px;height:87px;border-bottom:1px solid var(--line)}
.moulding .thumb{position:absolute;left:9px;top:11px;width:57px;height:62px;background:linear-gradient(90deg,#a8603f,var(--wood-dark) 40%,#b36d4a 70%,#7a4129)}
.moulding .name{position:absolute;left:86px;top:29px;font-size:10.5px;letter-spacing:1.2px}
.moulding .type{position:absolute;left:86px;top:44px;font-size:12.5px;letter-spacing:1.4px;color:var(--green)}
.scrollbar{left:357px;top:370px;width:12px;height:372px;background:#fff}
.scroll-thumb{left:357px;top:412px;width:12px;height:50px;border-radius:6px;background:var(--green-bright)}

.preview-label{left:382px;top:329px}
.frame-preview{left:495px;top:355px;width:362px;height:360px;background:linear-gradient(135deg,#f4ddc8,var(--wood) 50%,#f6e3d2)}
.frame-preview .photo{position:absolute;left:35px;top:37px;width:287px;height:288px;border:3px solid #5a3c2a;border-radius:10px;background:linear-gradient(#8aa0a8 0%,#5a6a40 40%,#3f5a22 70%,#a88a30 100%)}

.style-card{top:783px;width:215px}
.style-card h3{font-family:"Oswald",sans-serif;font-weight:400;font-size:21px;letter-spacing:1px;color:var(--green-bright);line-height:24px}
.style-card p{font-family:"Oswald",sans-serif;font-size:13px;letter-spacing:1.3px;color:#444;margin-top:2px}
.style-frame{top:840px;width:212px;height:210px;background:linear-gradient(135deg,#e9bf9e,#f6dcc6 50%,#ecc7a8)}
.style-frame .photo{position:absolute;left:19px;top:18px;width:175px;height:173px;border:7px solid #111;background:linear-gradient(#f2f2ee 0%,#7a7672 30%,#6a5d50 70%,#8a6a4e 100%)}

.site-footer{left:107px;top:1100px;width:981px;height:110px;border:7px solid #fff;border-radius:14px;background:linear-gradient(90deg,#e9b86f,#efc17c 40%,#e2ab5f 80%,#e9b56a)}
.footer-links{left:137px;top:1132px;word-spacing:12px;color:#4a3a20}
.copyright{left:137px;top:1168px;color:#4a3a20}
</style>
</head>
<body>

<header class="abs site-header"></header>
<nav class="abs nav-left caps green"><span>Lorem Ipsum</span><span>Lorem Ipsum</span></nav>
<div class="abs brand"><span class="brand-dot"></span>LUMAeco</div>
<nav class="abs nav-right caps">Sign In | Sign Up | Help |</nav>

<div class="abs breadcrumb caps">Home &gt; Lorem Ipsum &gt; Lorem Ipsum &gt; <span class="green">Lorem Ipsum</span></div>

<svg class="abs steps" width="702" height="48" viewBox="0 0 702 48" font-family="Open Sans, sans-serif">
  <rect x="0.5" y="0.5" width="700" height="46" fill="#fafafa" stroke="#d0d0d0"/>
  <polygon points="237,0 458,0 470,23.5 458,47 237,47 249,23.5" fill="#7cbf2a" stroke="#5c9a18"/>
  <polyline points="237,0 249,23.5 237,47" fill="none" stroke="#cfcfcf" stroke-width="2"/>
  <polyline points="458,0 470,23.5 458,47" fill="none" stroke="#cfcfcf" stroke-width="2"/>
  <circle cx="24" cy="24" r="13" fill="#fff" stroke="#ccc"/>
  <text x="24" y="28" font-size="11" text-anchor="middle" fill="#4d8f12">01</text>
  <text x="50" y="20" font-size="9.5" fill="#888">LOREM IPSUM DOLOR SIT</text>
  <text x="50" y="33" font-size="9.5" fill="#bbb">Nulla consequat massa quis enim</text>
  <circle cx="270" cy="24" r="13" fill="#fff" stroke="#5c9a18"/>
  <text x="270" y="28" font-size="11" text-anchor="middle" fill="#4d8f12">02</text>
  <text x="295" y="20" font-size="9.5" fill="#fff">LOREM IPSUM DOLOR SIT</text>
  <text x="295" y="33" font-size="9.5" fill="#fff">Nulla consequat massa quis enim</text>
  <circle cx="492" cy="24" r="13" fill="#fff" stroke="#ccc"/>
  <text x="492" y="28" font-size="11" text-anchor="middle" fill="#4d8f12">03</text>
  <text x="522" y="20" font-size="9.5" fill="#888">LOREM IPSUM DOLOR SIT</text>
  <text x="522" y="33" font-size="9.5" fill="#bbb">Nulla consequat massa quis enim</text>
</svg>

<section class="abs workspace"></section>
<div class="abs toolbar"></div>
<div class="abs toolbar-label caps">Lorem Ipsum: <span class="green">8"x8" Lorem Ipsum</span></div>
<svg class="abs tool-icons" width="120" height="28" viewBox="0 0 120 28" fill="none" stroke="#111" stroke-width="2.5">
  <rect x="6" y="6" width="14" height="14" transform="rotate(45 13 13)"/>
  <line x1="4" y1="13" x2="22" y2="13" stroke-width="2"/>
  <path d="M49 22 C49 13 55 10 64 10" stroke-width="3.5"/>
  <polygon points="62,3 70,10 62,17" fill="#111" stroke="none"/>
  <path d="M96 9 C96 4 108 4 108 10 C108 14 102 14 102 19"/>
  <circle cx="102" cy="25" r="1.8" fill="#111" stroke="none"/>
</svg>
<div class="abs btn-next">next</div>

<div class="abs sidebar-head"></div>
<div class="abs select"></div>
<div class="abs moulding-list">
  <div class="moulding" style="top:0"><div class="thumb" role="img" aria-label="Bamboo moulding sample"></div><div class="name">LOREM IPSUM</div><div class="type">LOREM IPSUM</div></div>
  <div class="moulding" style="top:87px"><div class="thumb" role="img" aria-label="Bamboo moulding sample"></div><div class="name">LOREM IPSUM</div><div class="type">LOREM IPSUM</div></div>
  <div class="moulding" style="top:174px"><div class="thumb" role="img" aria-label="Bamboo moulding sample"></div><div class="name">LOREM IPSUM</div><div class="type">LOREM IPSUM</div></div>
  <div class="moulding" style="top:261px"><div class="thumb" role="img" aria-label="Bamboo moulding sample"></div><div class="name">LOREM IPSUM</div><div class="type">LOREM IPSUM</div></div>
</div>
<div class="abs scrollbar"></div>
<div class="abs scroll-thumb"></div>

<div class="abs preview-label caps">Lorem Ipsum: <span class="green">Lorem Ipsum</span></div>
<div class="abs frame-preview"><div class="photo" role="img" aria-label="Uploaded photo: a child standing among tropical plants and palm trees"></div></div>

<div class="abs style-card" style="left:158px"><h3>LOREM IPSUM</h3><p>lorem ipsum dolor sit amet</p></div>
<div class="abs style-card" style="left:397px"><h3>LOREM IPSUM</h3><p>lorem ipsum dolor sit amet</p></div>
<div class="abs style-card" style="left:637px"><h3>LOREM IPSUM</h3><p>lorem ipsum dolor sit amet</p></div>
<div class="abs style-card" style="left:882px"><h3>LOREM IPSUM</h3><p>lorem ipsum dolor sit amet</p></div>

<div class="abs style-frame" style="left:133px"><div class="photo" role="img" aria-label="Framed photo of a couple in front of a wooden barn"></div></div>
<div class="abs style-frame" style="left:372px"><div class="photo" role="img" aria-label="Framed photo of a couple in front of a wooden barn"></div></div>
<div class="abs style-frame" style="left:612px"><div class="photo" role="img" aria-label="Framed photo of a couple in front of a wooden barn"></div></div>
<div class="abs style-frame" style="left:857px"><div class="photo" role="img" aria-label="Framed photo of a couple in front of a wooden barn"></div></div>

<footer class="abs site-footer"></footer>
<div class="abs footer-links caps">Lorem Ipsum | Lorem Ipsum | Lorem Ipsum | Lorem Ipsum | Lorem Ipsum</div>
<div class="abs copyright caps">Copyright 2012 LUMAeco Frame Company</div>

</body>
</html>
```